Tallowreed Advisory Partners Business Card Design

We have the logo we just need someone to design a modern business card design.

Name: Desmond Munkalt
Phone: 3055550148
Mobile: 9175550193
Web:www.tallowreedadvisory.example
email: dmunkalt@tallowreedadvisory.example
Company: Tallowreed Advisory Partners
Title: CEO

Address: 718 Quillmore Ave, Miami, Florida 33190

Target Market(s)

companies over 100 employees

Industry/Entity Type

Business

```html
<!DOCTYPE html>
<html lang="en">
<head>
<meta charset="utf-8">
<title>Tallowreed Advisory Partners – Business Card</title>
<link rel="stylesheet" href="https://fonts.googleapis.com/css2?family=Arimo:wght@400;600;700&family=PT+Sans:wght@400;700&display=swap">
<style>
  :root {
    --backdrop: #ecebe8;
    --paper: #ffffff;
    --paper-shade: #f1f1f1;
    --ink-dark: #0c0f12;
    --ink-mid: #1a1e22;
    --brand-blue: #3f65b5;
    --brand-grey: #5a5a5a;
    --back-grey: #6d6f72;
    --light-text: #f2f2f2;
  }
  * { box-sizing: border-box; margin: 0; padding: 0; }
  html, body {
    width: 1200px; height: 899px; overflow: hidden;
    background: var(--backdrop);
  }
  .canvas { position: relative; width: 1200px; height: 899px; }

  .card {
    position: absolute; width: 637px; height: 363px;
    box-shadow: 0 4px 10px rgba(0,0,0,.25);
    overflow: hidden;
  }
  .card--front { left: 122px; top: 86px; }
  .card--back {
    left: 464px; top: 471px;
    background: radial-gradient(ellipse at 50% 50%, var(--ink-mid) 0%, var(--ink-dark) 75%);
  }

  .front-top {
    position: absolute; left: 0; top: 0; width: 100%; height: 186px;
    background: linear-gradient(135deg, var(--paper) 0%, var(--paper-shade) 100%);
  }
  .front-rule { position: absolute; left: 0; top: 186px; width: 100%; height: 4px; background: var(--brand-blue); }
  .front-bottom {
    position: absolute; left: 0; top: 190px; width: 100%; height: 173px;
    background: linear-gradient(180deg, var(--ink-mid), var(--ink-dark));
  }

  .brand { position: absolute; text-align: center; font-family: "Arimo", sans-serif; font-weight: 700; color: var(--brand-grey); }
  .brand__dot { display: block; margin: 0 auto; border-radius: 50%; background: var(--brand-blue); }
  .brand__name { display: block; letter-spacing: .5px; line-height: 1; }
  .brand__sub { display: block; letter-spacing: .6px; line-height: 1; }

  .card--front .brand { left: 0; width: 100%; top: 27px; }
  .card--front .brand__dot { width: 80px; height: 80px; }
  .card--front .brand__name { font-size: 28px; margin-top: 14px; }
  .card--front .brand__sub { font-size: 10px; margin-top: 4px; }

  .card--back .brand { left: 0; width: 100%; top: 95px; color: var(--back-grey); }
  .card--back .brand__dot { width: 94px; height: 94px; }
  .card--back .brand__name { font-size: 33px; margin-top: 18px; }
  .card--back .brand__sub { font-size: 12px; margin-top: 5px; }

  .holder { position: absolute; left: 27px; top: 252px; font-family: "Arimo", sans-serif; color: var(--light-text); }
  .holder__name { font-size: 27px; font-weight: 400; line-height: 1.1; }
  .holder__title { font-size: 16px; margin-top: 3px; color: #d8d8d8; }

  .contacts { position: absolute; left: 306px; top: 208px; list-style: none; font-family: "PT Sans", sans-serif; }
  .contacts li { display: flex; align-items: center; height: 37px; color: var(--light-text); font-size: 15px; }
  .contacts svg { width: 22px; height: 20px; margin-right: 8px; fill: none; stroke: var(--light-text); stroke-width: 1.6; }

  .back-url {
    position: absolute; left: 0; width: 100%; top: 316px; text-align: center;
    font-family: "PT Sans", sans-serif; font-size: 16px; color: var(--back-grey); letter-spacing: .2px;
  }
</style>
</head>
<body>
<main class="canvas">
  <section class="card card--front" aria-label="Business card front">
    <div class="front-top" role="img" aria-label="Light paper texture area"></div>
    <div class="front-rule"></div>
    <div class="front-bottom"></div>
    <div class="brand">
      <span class="brand__dot"></span>
      <span class="brand__name">TALLOWREED</span>
      <span class="brand__sub">ADVISORY PARTNERS</span>
    </div>
    <div class="holder">
      <p class="holder__name">Desmond Munkalt</p>
      <p class="holder__title">Chief Executive Officer</p>
    </div>
    <ul class="contacts">
      <li><svg viewBox="0 0 24 24"><path d="M6 3l4 4-2 3c1 3 3 5 6 6l3-2 4 4-3 3C10 20 4 14 3 6z"/></svg>305.555.0148</li>
      <li><svg viewBox="0 0 24 24"><rect x="7" y="2" width="10" height="20" rx="1.5"/><line x1="7" y1="17" x2="17" y2="17"/></svg>917.555.0193</li>
      <li><svg viewBox="0 0 24 24"><circle cx="12" cy="12" r="9"/><ellipse cx="12" cy="12" rx="4" ry="9"/><line x1="3" y1="12" x2="21" y2="12"/></svg>www.tallowreedadvisory.example</li>
      <li><svg viewBox="0 0 24 24"><rect x="2" y="5" width="20" height="14"/><path d="M2 5l10 8 10-8M2 19l8-7M22 19l-8-7"/></svg>dmunkalt@tallowreedadvisory.example</li>
    </ul>
  </section>

  <section class="card card--back" aria-label="Business card back">
    <div class="brand">
      <span class="brand__dot"></span>
      <span class="brand__name">TALLOWREED</span>
      <span class="brand__sub">ADVISORY PARTNERS</span>
    </div>
    <p class="back-url">www.tallowreedadvisory.example</p>
  </section>
</main>
</body>
</html>
```